SEO marketing site

I need a design only for an SEO/Marketing project I have in mind. I have bought the domain Brivvora.example and want to aim this project at businesses who want to push their business further. WHEN I SAY DESIGN ONLY, I MEAN NO PROGRAMMING. HOWEVER, I DO NEED THE DESIGNER TO PUT THIS SITE ONLINE. $300 IS A LOT OF MONEY FOR A TEMPLATE YOU CAN PURCHASE FOR $60 WITH SOME CUSTOMISATION.

The idea is that businesses will register with us and will be offered two different kinds of services. They can make use of our scripts to check their back links, rankings, compare with competitors and a number of other marketing tools. The other service we provide is that we offer them an SEO service at a very competitive price. We will handle social networking, link building, article submission, directory submission, social bookmarking etc etc at a reasonable monthly fee.

I qoros tram look/flat design is what I really like, and I want to give off a professional vibe. This is the kind of site I wish to go for.

JUST TO REPEAT, I NEED A DESIGN TO BE PUT ONLINE, I.E PSD TO HTML CONVERSION. MY PROGRAMMERS WILL CODE THE CLIENT AREA THEMSELVES.

Target Market(s)

Other businesses

Industry/Entity Type

Marketing

Requirements
Must have
• Qoros 8 or flat design look. Even a site, similar to makerhive, is quite attractive. I would like a killer design for the site.

```html
<!DOCTYPE html>
<html lang="en">
<head>
<meta charset="utf-8">
<title>Brivvora – SEO &amp; Marketing</title>
<link rel="stylesheet" href="https://fonts.googleapis.com/css2?family=Open+Sans:wght@300;400;600;700&display=swap">
<style>
:root{
  --ink:#333333;
  --muted:#8a8a8a;
  --orange:#f47b10;
  --green:#7ac51f;
  --green-light:#93d332;
  --feature-green:#6cb524;
  --grey-band:#efeff1;
  --footer:#262626;
  --footer-text:#9a9a9a;
  --line:#e3e3e3;
  --client:#a8a8a8;
  --white:#ffffff;
}
*{margin:0;padding:0;box-sizing:border-box}
html,body{width:1200px;height:2483px;overflow:hidden}
body{font-family:"Open Sans",Arial,sans-serif;color:var(--ink);background:var(--white);position:relative}
.section{position:absolute;left:0;width:1200px}

/* header */
.site-header{top:0;height:119px;background:linear-gradient(#242424,#111)}
.brand{position:absolute;left:76px;top:24px;color:var(--white)}
.brand-name{display:block;font-size:40px;font-weight:400;line-height:48px;letter-spacing:.5px}
.brand-slogan{display:block;font-size:15px;font-weight:400;margin:4px 0 0 46px;color:var(--white)}
.main-nav{position:absolute;left:458px;top:56px;display:flex;gap:36px}
.main-nav a{color:#d8d8d8;text-decoration:none;font-size:16px;letter-spacing:.3px}
.signup{position:absolute;left:1037px;top:51px;width:99px;height:32px;border-radius:3px;background:var(--orange);color:var(--white);font-size:14px;font-weight:600;text-align:center;line-height:32px}

/* hero */
.hero{top:119px;height:498px;overflow:hidden}
.hero-photo{position:absolute;inset:0;background:radial-gradient(ellipse at 50% 70%,#ececec 0%,#cfcfcf 30%,#7d6a5c 60%,#2e2520 100%)}
.hero-devices{position:absolute;left:265px;top:188px;width:700px;height:310px;background:linear-gradient(#f4f4f4,#e2e2e2);border:14px solid #222;border-bottom:none;border-radius:10px 10px 0 0}
.hero-title{position:absolute;top:54px;width:100%;text-align:center;color:var(--white);font-size:40px;font-weight:300}
.hero-sub{position:absolute;top:112px;width:100%;text-align:center;color:var(--white);font-size:14px;letter-spacing:.4px}
.slide-arrow{position:absolute;top:222px;width:52px;height:52px;border-radius:50%;background:var(--white)}
.slide-arrow svg{position:absolute;left:18px;top:16px}
.prev{left:34px}.next{left:1120px}

/* testimonial band */
.quote-band{top:617px;height:113px;background:linear-gradient(var(--green-light),var(--green))}
.quote-text{position:absolute;left:148px;top:24px;width:660px;color:var(--white);font-size:18px;font-weight:300;line-height:30px}
.quote-divider{position:absolute;left:829px;top:21px;width:1px;height:70px;background:rgba(255,255,255,.8)}
.quote-name{position:absolute;left:864px;top:24px;color:var(--white);font-size:23px;font-weight:600}
.quote-role{position:absolute;left:866px;top:56px;color:var(--white);font-size:14px;font-weight:300}

/* intro */
.intro{top:730px;height:222px;border-bottom:1px solid var(--line);text-align:center}
.section-title{font-size:35px;font-weight:300;color:var(--ink)}
.intro .section-title{margin-top:47px}
.intro-text{width:960px;margin:14px auto 0;font-size:13.5px;line-height:25px;color:#777}

/* features */
.features{top:952px;height:422px}
.features-title{position:absolute;left:62px;top:47px;color:var(--feature-green);font-size:36px;font-weight:300;line-height:49px}
.features-text{position:absolute;left:64px;top:158px;width:420px;font-size:13.5px;line-height:24px;color:var(--muted)}
.features-text p+p{margin-top:9px}
.btn-orange{position:absolute;left:64px;top:300px;width:138px;height:38px;border-radius:4px;background:var(--orange);color:var(--white);font-size:15px;font-weight:600;text-align:center;line-height:38px}
.laptop{position:absolute;left:463px;top:40px;width:737px;height:382px}
.laptop-screen{position:absolute;left:100px;top:0;width:535px;height:368px;border-radius:14px 14px 0 0;background:#3a3a3a;padding:24px 28px 30px}
.laptop-display{width:100%;height:100%;background:linear-gradient(135deg,#f7f7f7,#e9eef2)}
.laptop-base{position:absolute;left:0;top:366px;width:737px;height:14px;border-radius:0 0 60px 60px;background:linear-gradient(#d6d6d6,#8c8c8c)}

/* services */
.services{top:1374px;height:485px;background:var(--grey-band);text-align:center}
.services .section-title{margin-top:50px}
.services-text{width:880px;margin:14px auto 0;font-size:13px;line-height:22px;color:var(--muted)}
.service-list{position:absolute;left:136px;top:182px;display:flex}
.service{width:232px;text-align:center}
.service-icon{width:114px;height:114px;border-radius:50%;background:var(--white);margin:0 auto;display:flex;align-items:center;justify-content:center}
.service-name{margin-top:14px;font-size:17px;color:#444}
.service-desc{font-size:13px;color:var(--muted);margin-top:2px}
.carousel-arrow{position:absolute;top:232px}
.c-prev{left:64px}.c-next{left:1100px}

/* clients */
.clients{top:1859px;height:251px;text-align:center}
.clients .section-title{margin-top:34px;font-size:31px}
.client-row{display:flex;justify-content:center;gap:56px;margin-top:24px;font-size:30px;font-weight:600;color:var(--client)}
.client-row.second{margin-top:22px}

/* footer */
.site-footer{top:2110px;height:373px;background:var(--footer)}
.footer-col{position:absolute;top:60px}
.footer-col h4{color:var(--white);font-size:18px;font-weight:400;margin-bottom:12px;letter-spacing:.3px}
.footer-col li{list-style:none;color:var(--footer-text);font-size:13.5px;line-height:25px}
.footer-col p{color:var(--footer-text);font-size:13px;line-height:22px;width:300px}
.newsletter{display:flex;margin-top:12px}
.newsletter span{display:block;width:186px;height:28px;background:var(--white);color:#999;font-size:12px;line-height:28px;padding-left:10px}
.newsletter b{display:block;width:95px;height:28px;background:var(--orange);color:var(--white);font-weight:400;font-size:14px;line-height:28px;text-align:center}
.social{display:flex;gap:6px;margin-top:12px}
.social i{display:block;width:30px;height:30px;border-radius:50%;background:#555}
.footer-rule{position:absolute;left:70px;top:286px;width:1082px;height:1px;background:#3c3c3c}
.copyright{position:absolute;left:70px;top:315px;color:#7d7d7d;font-size:12.5px}
</style>
</head>
<body>

<header class="section site-header">
  <div class="brand">
    <span class="brand-name">Brivvora</span>
    <span class="brand-slogan">slogan goes here</span>
  </div>
  <nav class="main-nav">
    <a href="#">HOME</a><a href="#">FEATURES</a><a href="#">ABOUT</a><a href="#">BLOG</a><a href="#">SERVICE</a><a href="#">CONTACT</a>
  </nav>
  <div class="signup">SIGN UP</div>
</header>

<section class="section hero">
  <div class="hero-photo" role="img" aria-label="Blurred office background photograph"></div>
  <div class="hero-devices" role="img" aria-label="Tablet and monitor showing marketing strategy sketches"></div>
  <h1 class="hero-title">Class aptent taciti sociosqu ad litora torquent</h1>
  <p class="hero-sub">PHASELLUS FELIS DOLOR SCELERISQUE A TEMPUS EGET LOBORTIS ID LIBERO.</p>
  <div class="slide-arrow prev"><svg width="16" height="20" viewBox="0 0 16 20"><path d="M11 2 3 10l8 8" fill="none" stroke="#333" stroke-width="2.5"/></svg></div>
  <div class="slide-arrow next"><svg width="16" height="20" viewBox="0 0 16 20"><path d="M5 2l8 8-8 8" fill="none" stroke="#333" stroke-width="2.5"/></svg></div>
</section>

<section class="section quote-band">
  <p class="quote-text">“Suspendisse vulputate aliquam dui. Nulla elementum dui ut augue. Aliquam vehicula mi at mauris Maecenas placerat nisl at consequat”</p>
  <div class="quote-divider"></div>
  <div class="quote-name">DANE CORLETT</div>
  <div class="quote-role">IT Development</div>
</section>

<section class="section intro">
  <h2 class="section-title">Mauris vel lacus vitae felis vestibulum</h2>
  <p class="intro-text">They can make use of our scripts to check their back links, rankings, compare with competitors and a number of other marketing tools.. Donec scelerisque leo ac risus. Praesent sit amet est. In dictum, dolor eu dictum porttitor, enim felis viverra mi, eget luctus massa purus quis odio. Etiam nulla massa, pharetra facilisis, volutpat in, imperdiet sit amet, sem. Aliquam nec erat at purus cursus interdum</p>
</section>

<section class="section features">
  <h2 class="features-title">Comprehensive Features<br>and Social Business</h2>
  <div class="features-text">
    <p>Mauris vel lacus vitae felis vestibulum volutpat. Etiam est nunc, venenatis in, tristique eu, imperdiet ac, nisl. Cum sociis natoque penatibus et magnis dis parturient montes</p>
    <p>Class aptent taciti sociosqu ad litora torquent per conubia nostra, per inceptos hymenaeos. Proin nulla arcu, nonummy luctus</p>
  </div>
  <div class="btn-orange">FREE TRAIL</div>
  <div class="laptop">
    <div class="laptop-screen"><div class="laptop-display" role="img" aria-label="Laptop screen showing social analytics infographics"></div></div>
    <div class="laptop-base"></div>
  </div>
</section>

<section class="section services">
  <h2 class="section-title">What We Provide</h2>
  <p class="services-text">Morbi eget arcu. Morbi porta, libero id ullamcorper nonummy, nibh ligula pulvinar metus, eget consectetuer augue nisi quis lacus. Ut ac mi quis lacus mollis aliquam. Curabitur iaculis tempus eros. Curabitur vel mi sit amet magna malesuada ultrices.</p>
  <svg class="carousel-arrow c-prev" width="40" height="90" viewBox="0 0 40 90"><path d="M38 2 2 45l36 43" fill="none" stroke="#b9b9b9" stroke-width="2"/></svg>
  <svg class="carousel-arrow c-next" width="40" height="90" viewBox="0 0 40 90"><path d="M2 2l36 43L2 88" fill="none" stroke="#b9b9b9" stroke-width="2"/></svg>
  <div class="service-list">
    <div class="service">
      <div class="service-icon"><svg width="62" height="62" viewBox="0 0 62 62" fill="none" stroke="#f47b10" stroke-width="2.5"><circle cx="31" cy="31" r="17"/><ellipse cx="31" cy="31" rx="7" ry="17"/><path d="M14 31h34M17 22h28M17 40h28M31 2v8M31 52v8M2 31h8M52 31h8"/></svg></div>
      <div class="service-name">Social Networking</div>
      <div class="service-desc">Phasellus felis dolor, scelerisque</div>
    </div>
    <div class="service">
      <div class="service-icon"><svg width="62" height="54" viewBox="0 0 62 54" fill="none" stroke="#f47b10" stroke-width="2.5"><rect x="18" y="4" width="40" height="28"/><path d="M12 10v28h40M6 16v28h40"/></svg></div>
      <div class="service-name">Link building</div>
      <div class="service-desc">Phasellus felis dolor scelerisque</div>
    </div>
    <div class="service">
      <div class="service-icon"><svg width="52" height="58" viewBox="0 0 52 58" fill="none" stroke="#f47b10" stroke-width="2.5"><rect x="6" y="8" width="40" height="46"/><path d="M14 3v10M26 3v10M38 3v10M14 24h24M14 32h24M14 40h24"/></svg></div>
      <div class="service-name">Article Submission</div>
      <div class="service-desc">PhasTempus eget, lobortis</div>
    </div>
    <div class="service">
      <div class="service-icon"><svg width="62" height="58" viewBox="0 0 62 58" fill="none" stroke="#f47b10" stroke-width="2.5"><rect x="32" y="3" width="26" height="18" rx="2"/><path d="M40 21l-4 6 10-6"/><circle cx="24" cy="26" r="10"/><path d="M6 54c0-12 8-18 18-18s18 6 18 18z"/></svg></div>
      <div class="service-name">Social Bookmarking</div>
      <div class="service-desc">Phasellus felis dolor scelerisque</div>
    </div>
  </div>
</section>

<section class="section clients">
  <h2 class="section-title">Our Clients &amp; Partners</h2>
  <div class="client-row">
    <span>Quillpress</span><span>Arkspan</span><span>Tallyframe</span><span>Vellum Ads</span>
  </div>
  <div class="client-row second"><span>Pixelward Hub</span></div>
</section>

<footer class="section site-footer">
  <div class="footer-col" style="left:76px">
    <h4>FEATURES</h4>
    <ul><li>Home</li><li>Features</li><li>Plans &amp; Pricing</li><li>Case Studies</li><li>Affiliate Program</li></ul>
  </div>
  <div class="footer-col" style="left:268px">
    <h4>COMPANY</h4>
    <ul><li>Support</li><li>FAQ</li><li>About Us</li><li>What We Do</li><li>Services Provide</li></ul>
  </div>
  <div class="footer-col" style="left:459px">
    <h4>SUPPORT</h4>
    <ul><li>Terms of Service</li><li>Use of cookies</li><li>Blog</li><li>Startups</li></ul>
  </div>
  <div class="footer-col" style="left:662px">
    <h4>DOWNLOAD</h4>
    <ul><li>Mobile</li><li>Tablet</li><li>Handheld</li></ul>
  </div>
  <div class="footer-col" style="left:853px">
    <h4>FEATURES</h4>
    <p>Subscribe to our newsletter! Get productivity tips, product updates and special offers.</p>
    <div class="newsletter"><span>email address</span><b>Subscribe</b></div>
    <div class="social"><i></i><i></i><i></i><i></i></div>
  </div>
  <div class="footer-rule"></div>
  <div class="copyright">© 2013 Company Name.  All right reserved.  Term of Use</div>
</footer>

</body>
</html>
```